Christmas Web Slider

We need a new clean and quality Christmas Slider for our home page (https://www.plumverdant.co.uk/) to engage customers to interact with our Christmas ranges. It will link to our All Christmas Products department page. Must be within the specs of our current sliders for size and be minimal in memory size to avoid slowing the web page load time down.

Target Market(s)

home and business users but more home public for this product category

Industry/Entity Type

artificial Christmas trees and related Chirtmas products and decor

Colors
00AB8E
00BBA5
67D7C9
C6EFE9
E9F9F6
FFC000
F8CF3A
FAE287
FDF2CF
FEFAEE
EB3D1F
EC4F4E
F09395
F8D3D4
FCEDEE

Requirements
Must have
• typical festive imagery and text to engage and draw the visitor in to click
Nice to have
• obvious call to actions
Should not have
• anyhting cheap or tacky

```html
<!DOCTYPE html>
<html lang="en">
<head>
<meta charset="utf-8">
<title>Christmas Web Slider – Trees, Gifts &amp; Decor</title>
<link rel="stylesheet" href="https://fonts.googleapis.com/css2?family=Allura&family=Montserrat:wght@700&family=Playfair+Display:wght@900&family=Poppins:wght@600&display=swap">
<style>
  :root {
    --page-bg: #FFFFFF;
    --red: #EB3D1F;
    --deep-teal: #0D3D36;
    --teal: #4EC3AE;
    --cream: #FDF9EC;
    --glow: #FDEFD9;
    --ground: #F3CFA0;
    --gold: #F9BF00;
    --cta-text: #5A4000;
    --shadow: #E6E6E6;
  }
  * { box-sizing: border-box; margin: 0; padding: 0; }
  html, body {
    width: 1200px; height: 854px; overflow: hidden;
    background: var(--page-bg);
  }
  .board { position: relative; width: 1200px; height: 854px; }

  .board-title {
    position: absolute; top: 128px; left: 0; width: 100%;
    text-align: center;
    font-family: "Montserrat", sans-serif; font-weight: 700;
    font-size: 39px; letter-spacing: 1.5px; color: var(--red);
  }
  .board-size {
    position: absolute; top: 188px; left: 0; width: 100%;
    text-align: center;
    font-family: "Montserrat", sans-serif; font-weight: 700;
    font-size: 23px; letter-spacing: 1px; color: var(--deep-teal);
  }

  .banner-shadow {
    position: absolute; left: 102px; top: 281px;
    width: 992px; height: 496px;
    background: var(--shadow); filter: blur(3px);
  }
  .banner {
    position: absolute; left: 118px; top: 265px;
    width: 992px; height: 496px;
    background: var(--cream); overflow: hidden;
  }

  .headline {
    position: absolute; left: 25px; top: 80px; width: 500px;
    text-align: center;
    font-family: "Allura", cursive; font-weight: 400;
    font-size: 142px; line-height: 1; color: var(--red);
    white-space: nowrap;
  }
  .range {
    position: absolute; left: 82px; top: 242px; width: 382px;
    text-align: center;
    font-family: "Playfair Display", serif; font-weight: 900;
    font-size: 32px; color: var(--teal); white-space: nowrap;
  }
  .offer {
    position: absolute; left: 82px; top: 290px; width: 382px;
    text-align: center;
    font-family: Arial, Helvetica, sans-serif; font-style: italic;
    font-size: 28px; color: var(--red);
  }
  .cta {
    position: absolute; left: 121px; top: 349px;
    width: 303px; height: 63px;
    display: flex; align-items: center; justify-content: center;
    background: var(--gold); color: var(--cta-text);
    font-family: "Poppins", sans-serif; font-weight: 600;
    font-size: 31px; text-decoration: none;
  }

  .tree-art {
    position: absolute; left: 574px; top: 71px;
    width: 362px; height: 342px;
  }
  .tree-art svg { display: block; width: 100%; height: 100%; }
</style>
</head>
<body>
  <main class="board">
    <h1 class="board-title">WEB SLIDER BANNER - MOCKUP 2</h1>
    <p class="board-size">SIZE: 1240PX(WIDTH) X 620PX (HEIGHT)</p>

    <div class="banner-shadow"></div>
    <section class="banner">
      <h2 class="headline">Christmas</h2>
      <p class="range">TREES, GIFTS &amp; DECOR</p>
      <p class="offer">UPTO 50% OFF</p>
      <a class="cta" href="https://www.plumverdant.co.uk/">SHOP NOW</a>

      <div class="tree-art" role="img" aria-label="Illustrated decorated Christmas tree with a gold star, baubles and wrapped gifts beneath it, set in a soft cream circle">
        <svg viewBox="0 0 362 342" aria-hidden="true">
          <defs>
            <radialGradient id="tree-glow" cx="50%" cy="55%" r="50%">
              <stop offset="0%" stop-color="#2E6A57"/>
              <stop offset="50%" stop-color="#9DB79E"/>
              <stop offset="100%" stop-color="#FDEFD9"/>
            </radialGradient>
          </defs>
          <circle cx="181" cy="178" r="158" fill="url(#tree-glow)"/>
          <ellipse cx="181" cy="322" rx="180" ry="18" fill="var(--ground)"/>
        </svg>
      </div>
    </section>
  </main>
</body>
</html>
```